Brava Set CEO and Partners Business Card

We need a fresh, fun, simple and clean business card design....we would like a template where we can add a name and title (as well as specific email addresses). We are open to different looks (full logo on one side and a small logo on the company info side, or our logo is in the background but faint on one side but full on the other, or something else cool :-) ). Our colors are in our logo: blue, black and white...however we are not opposed to the use of other colors if it works. We build sets, make props and a host of other things for the film and television industry...our card should reflect creativity, style and professionalism.

A white background would be preferred.

I would like to see an option with Facebook and Instagram icons.

Facebook- social-example.com/bravasetny
Instagram- brava_set

Our website is bravaset-example.com.

Brava Set, Inc.
418 Corvell Avenue, Unit 9
North Hollywood, California 91602
555.210.4873 | tel
555.210.6692 | fax
www.BravaSet-example.com

Sample Name and Title #1:

Peter Halvik
CEO / Co-Owner
555.210.4873 | tel
555.210.6692 | fax
peter@bravaset-example.com
www.BravaSet-example.com

Target Market(s)

Marketing Professionals, Production Designers, Interior Designers, Film Producers, Directors, Art Directors, Event Directors

Industry/Entity Type

Entertainment Industry

Contact Information for Business Card

Peter Halvik
CEO / Co-Owner
555.210.4873 | tel
555.210.6692 | fax
peter@bravaset-example.com
www.BravaSet-example.com

Font styles to use
Sans Serif

Colors
33a6d7
ffffff
1b1b1b

Requirements
Must have
• Logo, All Contact Info, White Background. Symmetry.
Nice to have
• Facebook and Instagram icons with addresses
• Facebook- social-example.com/bravasetny
• Instagram- brava_set

```html
<!DOCTYPE html>
<html lang="en">
<head>
<meta charset="utf-8">
<title>Brava Set — Business Card</title>
<link rel="stylesheet" href="https://fonts.googleapis.com/css2?family=Source+Sans+3:wght@400;600;700;800&display=swap">
<style>
  :root {
    --stage: #4a4a4a;
    --card-dark: #1f2022;
    --card-light: #abadac;
    --brand-blue: #33a6d7;
    --ink-white: #ffffff;
    --text-soft: #e6e6e6;
    --icon-dark: #1b1b1b;
  }
  * { margin: 0; padding: 0; box-sizing: border-box; }
  html, body {
    width: 1200px; height: 900px; overflow: hidden;
    background: var(--stage);
    font-family: "Source Sans 3", Arial, sans-serif;
  }
  .canvas { position: relative; width: 1200px; height: 900px; }
  .card {
    position: absolute; top: 270px; width: 457px; height: 282px;
    border-radius: 12px;
  }
  .card--front {
    left: 137px;
    background: repeating-linear-gradient(90deg, #212224 0 2px, #1d1e20 2px 4px);
  }
  .card--back { left: 626px; background: var(--card-light); }

  .wordmark {
    position: absolute; color: var(--ink-white); font-weight: 800;
    letter-spacing: -1px; line-height: 1; white-space: nowrap;
  }
  .card--front .wordmark { left: 22px; top: 30px; font-size: 56px; }
  .card--back .wordmark { left: 0; width: 100%; text-align: center; top: 62px; font-size: 70px; }

  .person { position: absolute; right: 20px; top: 136px; text-align: right; }
  .person__name { font-size: 21px; font-weight: 600; color: var(--ink-white); line-height: 1.1; }
  .person__surname { color: var(--brand-blue); }
  .person__title { font-size: 13px; color: var(--text-soft); margin-top: 4px; }

  .contact-list { position: absolute; left: 22px; top: 191px; list-style: none; }
  .contact-list li {
    display: flex; align-items: center; gap: 6px;
    font-size: 13px; color: var(--text-soft); height: 19px;
  }
  .contact-list svg { width: 9px; height: 9px; fill: var(--brand-blue); flex: none; }

  .address {
    position: absolute; right: 18px; top: 221px; text-align: right;
    font-size: 13px; line-height: 14px; color: var(--text-soft); font-style: normal;
  }
  .address__company { font-weight: 700; color: var(--ink-white); }

  .social { position: absolute; left: 0; width: 100%; top: 185px; text-align: center; }
  .social__icons { display: flex; justify-content: center; gap: 18px; }
  .social__icons span { width: 20px; height: 20px; background: var(--icon-dark); border-radius: 2px; }
  .social__links { margin-top: 12px; font-size: 14.5px; line-height: 19px; color: var(--ink-white); }
</style>
</head>
<body>
<main class="canvas">
  <section class="card card--front" aria-label="Card front">
    <div class="wordmark">Brava Set</div>

    <div class="person">
      <p class="person__name">Peter <span class="person__surname">Halvik</span></p>
      <p class="person__title">CEO / Co-Owner</p>
    </div>

    <ul class="contact-list">
      <li><svg viewBox="0 0 10 10" aria-hidden="true"><path d="M1 3c0-1 1-2 2-2h4c1 0 2 1 2 2v1H7V3H3v1H1zM2 5h6l1 4H1z"/></svg>555.210.4873</li>
      <li><svg viewBox="0 0 10 10" aria-hidden="true"><path d="M3 0h4v3H3zM1 3h8v5H7v2H3V8H1zM4 7v2h2V7z"/></svg>555.210.6692</li>
      <li><svg viewBox="0 0 10 10" aria-hidden="true"><path d="M0 2h10v1L5 6 0 3zM0 4l5 3 5-3v4H0z"/></svg>peter@bravaset-example.com</li>
      <li><svg viewBox="0 0 10 10" aria-hidden="true"><circle cx="5" cy="5" r="5"/></svg>www.BravaSet-example.com</li>
    </ul>

    <address class="address">
      <span class="address__company">Brava Set, Inc.</span><br>
      418 Corvell Avenue, Unit 9<br>
      North Hollywood, California 91602
    </address>
  </section>

  <section class="card card--back" aria-label="Card back">
    <div class="wordmark">Brava Set</div>
    <div class="social">
      <div class="social__icons" aria-hidden="true"><span></span><span></span></div>
      <p class="social__links">social-example.com/bravasetny<br>photos-example.com/brava_set</p>
    </div>
  </section>
</main>
</body>
</html>
```